Trade show banner and popup for Plexa Works

Use the existing logo and graphic elements and text of sales arguments from our web site www.plexaworks-demo.com to create a backdrop banner and popup banner.

Both banners are trim size 181.7 x 76.2 cm. One is vertical, the other is horizontal. The full bleed size is 767 x 1824 mm 2265 x 5385 pixels.

We have a 2m by 2m corner stand on a tradeshow. The banner will be on one wall, the vertical against the other wall by the aisle.

Target Market(s)

This display is for a manufacturing trade show. The typical visitors are middle age engineers.

Industry/Entity Type

Trade

Requirements
Must have
• Our logo.
Nice to have
• One of the main benefits of our system is that it can be created for no charge with an online signup which is available at the show. We want to tempt people off the aisles to do this. So the vertical banner could have the words "Create your own online ERP system here for no charge"
Should not have
• Small text, these banners should attract attention of passers by in a trade show.

```html
<!DOCTYPE html>
<html lang="en">
<head>
<meta charset="utf-8">
<title>Plexa Works – Trade Show Banner</title>
<link rel="stylesheet" href="https://fonts.googleapis.com/css2?family=Jost:wght@400;700&display=swap">
<style>
  :root {
    --page-bg: #ffffff;
    --sky-top: #f3f9ff;
    --sky-mid: #8fd3f4;
    --sky-low: #19b2ea;
    --sky-deep: #0a9fdc;
    --ink: #0b0b0b;
    --khaki: #c9c28e;
    --white: #ffffff;
  }
  html, body {
    margin: 0;
    width: 1200px;
    height: 900px;
    overflow: hidden;
    background: var(--page-bg);
  }
  .canvas {
    position: relative;
    width: 1200px;
    height: 900px;
  }
  .banner {
    position: absolute;
    left: 175px;
    top: 272px;
    width: 852px;
    height: 357px;
    overflow: hidden;
    box-shadow: 2px 3px 6px rgba(0, 0, 0, 0.35);
  }
  .banner__backdrop {
    position: absolute;
    inset: 0;
    background:
      radial-gradient(ellipse 60% 55% at 62% 30%, rgba(255,255,255,0.75), rgba(255,255,255,0) 70%),
      linear-gradient(180deg, var(--sky-top) 0%, var(--sky-mid) 35%, var(--sky-low) 65%, var(--sky-deep) 100%);
  }
  .brand-dot {
    position: absolute;
    left: 227px;
    top: 358px;
    width: 186px;
    height: 186px;
    margin: 0;
  }
  .brand-name {
    position: absolute;
    left: 444px;
    top: 330px;
    margin: 0;
    font-family: "Jost", sans-serif;
    font-weight: 700;
    font-size: 104px;
    line-height: 100px;
    color: var(--ink);
    letter-spacing: 1px;
  }
  .brand-name__line { display: block; }
  .brand-name__line--second { padding-left: 118px; }
  .tagline {
    position: absolute;
    left: 380px;
    top: 558px;
    margin: 0;
    font-family: "Jost", sans-serif;
    font-weight: 400;
    font-size: 25px;
    letter-spacing: -0.3px;
    color: var(--white);
    white-space: nowrap;
  }
</style>
</head>
<body>
<main class="canvas">
  <section class="banner" aria-label="Plexa Works banner">
    <div class="banner__backdrop" role="img" aria-label="Soft blue gradient background with faint flowing line texture"></div>
  </section>
  <svg class="brand-dot" viewBox="0 0 186 186" aria-hidden="true">
    <circle cx="93" cy="93" r="90" fill="var(--khaki)"/>
  </svg>
  <h1 class="brand-name">
    <span class="brand-name__line">Plexa</span>
    <span class="brand-name__line brand-name__line--second">Works</span>
  </h1>
  <p class="tagline">EASY • EFFICIENT • EVERYWHERE</p>
</main>
</body>
</html>
```